Sports Betting Business Consultant

After 21 years in corporate life. Will be continue as consultant/advisor in sports betting industry. Need a business card. Prefer an iphone format as layout. Elements; betting,ticket, sports types soccer, basketball, tennis etc , odds etc.

```html
<!DOCTYPE html>
<html lang="en">
<head>
<meta charset="utf-8">
<title>Deniz Aral — Business Card</title>
<link rel="stylesheet" href="https://fonts.googleapis.com/css2?family=Arimo:wght@400;700&display=swap">
<style>
  :root {
    --stage: #1a1a1a;
    --paper: #fbfbfa;
    --paper-shade: #eeeeec;
    --brand-red: #c24a4a;
    --brand-red-light: #d65c5c;
    --brand-red-dark: #a93c3c;
    --ink: #333333;
    --white: #ffffff;
  }
  * { box-sizing: border-box; margin: 0; padding: 0; }
  html, body {
    width: 1200px;
    height: 900px;
    overflow: hidden;
    background: var(--stage);
    font-family: "Arimo", Arial, sans-serif;
  }
  .canvas {
    width: 1200px;
    height: 900px;
    display: flex;
    flex-direction: column;
    align-items: center;
    justify-content: center;
    gap: 60px;
  }
  .card {
    position: relative;
    width: 600px;
    height: 310px;
    box-shadow: 0 18px 40px rgba(0,0,0,0.45);
  }

  /* Front side */
  .card-front {
    background: linear-gradient(175deg, var(--paper) 0%, var(--paper) 55%, var(--paper-shade) 100%);
  }
  .identity {
    position: absolute;
    top: 96px;
    left: 0;
    width: 100%;
    display: flex;
    justify-content: center;
    align-items: center;
    gap: 18px;
  }
  .holder-name {
    color: var(--brand-red);
    font-weight: 700;
    font-size: 21px;
    letter-spacing: 2.2px;
    white-space: nowrap;
  }
  .divider {
    width: 2px;
    height: 28px;
    background: var(--brand-red);
  }
  .contact {
    color: var(--ink);
    font-size: 14px;
    letter-spacing: 1.6px;
    line-height: 1.15;
    white-space: nowrap;
  }
  .stripes {
    position: absolute;
    left: 26px;
    right: 26px;
    bottom: 34px;
  }
  .stripe {
    height: 5px;
    margin-top: 6px;
  }
  .stripe-red { background: var(--brand-red); }
  .stripe-dark { background: var(--ink); }

  /* Back side */
  .card-back {
    background: linear-gradient(160deg, var(--brand-red-light) 0%, var(--brand-red) 50%, var(--brand-red-dark) 100%);
    display: flex;
    align-items: center;
    justify-content: center;
  }
  .back-name {
    color: var(--white);
    font-weight: 700;
    font-size: 14px;
    letter-spacing: 1.4px;
    padding-bottom: 3px;
    border-bottom: 1.5px solid var(--white);
    white-space: nowrap;
  }
</style>
</head>
<body>
  <main class="canvas">
    <section class="card card-front" aria-label="Card front">
      <div class="identity">
        <span class="holder-name">Deniz Aral</span>
        <span class="divider"></span>
        <div class="contact">
          <p class="phone">+90 555 0142200</p>
          <p class="email">dnzarl@mailbox.com</p>
        </div>
      </div>
      <div class="stripes">
        <div class="stripe stripe-red"></div>
        <div class="stripe stripe-dark"></div>
      </div>
    </section>

    <section class="card card-back" aria-label="Card back">
      <span class="back-name">Deniz Aral</span>
    </section>
  </main>
</body>
</html>
```